business card for glass company

logo on business card and letterhead. our business is installing and servicing glass and mirror in commercial and industrial buildings in the Toronto area. full company name, Halworth Glass and Mirror Ltd.
i am looking for a business card and letterhead design.
on the letterhead i need company name and contact info
Halworth Glass and Mirror Ltd.
718 Larchmere Rd.
Toronto, Ontario
M4K 7B9
on the cards the contact info is
Dana Halworth
718 Larchmere Rd.
Toronto, Ontario
M4K 7B9
(416) 555-0142
(416) 555 0187-cell
i need another card with different name
Martin Quell
594 Kemble St. N
Hamilton Ontario
L3R 9T2
(416) 555-0142
(416) 555-0163
Target Market(s)
Professionals in industrial and commercial building construction, architects, general contractors, building managers and owners.
Industry/Entity Type
Business
Requirements
Must have
- simple design with two colors. emphasis on the name Halworth.

```html
<!DOCTYPE html>
<html lang="en">
<head>
<meta charset="utf-8">
<title>Halworth Glass &amp; Mirror Ltd. – Stationery</title>
<link rel="stylesheet" href="https://fonts.googleapis.com/css2?family=Crimson+Pro:wght@400&family=Open+Sans:wght@400&display=swap">
<style>
  :root {
    --bar-grey: #a3a4a6;
    --bar-text: #ffffff;
    --ink: #3b3b3d;
    --mark-blue: #34527f;
    --paper: #ffffff;
    --card-edge: #9a9ca0;
    --frost: #dde3ee;
    --blue-deep: #3a5b8c;
    --blue-mid: #7f9fcc;
    --blue-light: #cfe0f2;
    --blue-night: #24496a;
  }
  html, body { margin: 0; padding: 0; overflow: hidden; }
  body { width: 1200px; height: 1200px; position: relative; background: var(--paper); font-family: "Crimson Pro", "Times New Roman", serif; color: var(--ink); }
  .board-bar { position: absolute; left: 0; width: 1200px; background: var(--bar-grey); }
  .board-bar--top { top: 0; height: 33px; color: var(--bar-text); font-family: "Open Sans", Arial, sans-serif; font-size: 18px; letter-spacing: 3px; text-align: center; line-height: 35px; }
  .board-bar--bottom { bottom: 0; height: 38px; }
  .backdrop {
    position: absolute; left: 18px; top: 52px; width: 1167px; height: 1088px;
    background:
      linear-gradient(160deg, rgba(255,255,255,0) 40%, rgba(255,255,255,.55) 52%, rgba(255,255,255,0) 66%),
      linear-gradient(125deg, var(--blue-mid) 0%, var(--blue-deep) 22%, var(--blue-light) 45%, var(--blue-mid) 62%, var(--blue-light) 76%, var(--blue-night) 100%);
  }
  .letterhead { position: absolute; left: 50px; top: 87px; width: 787px; height: 1020px; background: var(--paper); overflow: hidden; }
  .card { position: absolute; left: 750px; width: 383px; height: 234px; background: var(--paper); border: 1px solid var(--card-edge); overflow: hidden; box-sizing: border-box; }
  .card--dana { top: 415px; }
  .card--martin { top: 708px; }

  .brand { position: absolute; display: flex; align-items: center; }
  .brand__dot { border-radius: 50%; background: var(--mark-blue); flex: none; }
  .brand__text { display: flex; flex-direction: column; color: var(--ink); line-height: 1; white-space: nowrap; }
  .brand__sub { margin-top: 1px; }
  .brand--small .brand__dot { width: 40px; height: 40px; margin-right: 8px; }
  .brand--small .brand__name { font-size: 30px; }
  .brand--small .brand__sub { font-size: 13px; }
  .brand--hero { left: 867px; top: 196px; }
  .brand--hero .brand__dot { width: 78px; height: 78px; margin-right: 12px; }
  .brand--hero .brand__name { font-size: 52px; }
  .brand--hero .brand__sub { font-size: 23px; }
  .letterhead .brand { left: 553px; top: 44px; }
  .card .brand { left: 155px; top: 28px; }

  .address { position: absolute; margin: 0; font-size: 12px; line-height: 1; }
  .address span { display: block; }
  .letterhead .address { left: 607px; top: 128px; }
  .letterhead .address span { margin-bottom: 22px; }
  .card .address { left: 210px; top: 120px; font-size: 11px; }
  .card .address span { margin-bottom: 12px; }
  .card__person { position: absolute; left: 48px; top: 120px; margin: 0; font-size: 14px; line-height: 1; }
  .watermark-ring { position: absolute; border-radius: 50%; border-style: solid; border-color: var(--frost); opacity: .8; }
  .letterhead .watermark-ring { left: -40px; top: 600px; width: 360px; height: 360px; border-width: 26px; }
  .card .watermark-ring { left: 0; top: 108px; width: 90px; height: 90px; border-width: 8px; }
</style>
</head>
<body>
  <header class="board-bar board-bar--top">FOR YOUR APPROVAL</header>

  <div class="backdrop"></div>

  <section class="letterhead" aria-label="Letterhead">
    <div class="watermark-ring"></div>
    <div class="brand brand--small"><span class="brand__dot"></span><span class="brand__text"><span class="brand__name">Halworth</span><span class="brand__sub">Glass &amp; Mirror Ltd</span></span></div>
    <p class="address">
      <span>718 Larchmere Road,</span>
      <span>Toronto, Ontario M4K 7B9</span>
      <span>Phone: (416) 555-0142</span>
    </p>
  </section>

  <div class="brand brand--hero"><span class="brand__dot"></span><span class="brand__text"><span class="brand__name">Halworth</span><span class="brand__sub">Glass &amp; Mirror Ltd</span></span></div>

  <section class="card card--dana" aria-label="Business card, Dana Halworth">
    <div class="watermark-ring"></div>
    <div class="brand brand--small"><span class="brand__dot"></span><span class="brand__text"><span class="brand__name">Halworth</span><span class="brand__sub">Glass &amp; Mirror Ltd</span></span></div>
    <p class="card__person">Dana Halworth</p>
    <p class="address">
      <span>718 Larchmere Road,</span>
      <span>Toronto, Ontario M4K 7B9</span>
      <span>(416) 555-0142</span>
      <span>(416) 555-0187-cell</span>
    </p>
  </section>

  <section class="card card--martin" aria-label="Business card, Martin Quell">
    <div class="watermark-ring"></div>
    <div class="brand brand--small"><span class="brand__dot"></span><span class="brand__text"><span class="brand__name">Halworth</span><span class="brand__sub">Glass &amp; Mirror Ltd</span></span></div>
    <p class="card__person">Martin Quell</p>
    <p class="address">
      <span>594 Kemble St. N,</span>
      <span>Hamilton, Ontario L3R 9T2</span>
      <span>(416) 555-0142</span>
      <span>(416) 555-0163</span>
    </p>
  </section>

  <footer class="board-bar board-bar--bottom"></footer>
</body>
</html>
```